Bright Path Attorneys Billboard Design for Personal Injury Law Firm

Need a billboard design that we can use for different versions. 1400px X 400px jpeg or png
I have attached the logo and the attorney for the billboard. Attorney Marla Benning
Here is a link to our current website brightpathlegalgroup.example

HEADLINE: HIT BY A TRUCK?
SUBHEAD: NO FEE. BIG FIGHT.
877-GRANTLY

HEADLINE: ACCIDENT?
SUBHEAD: NO FEE, UNLESS WE WIN!
877-GRANTLY

HEADLINE: BIG TRUCK. BIG CASE.
SUBHEAD: YOU PAY $0 UPFRONT
877-GRANTLY

Target Market(s)

People in Car Accident

Industry/Entity Type

Personal Injury Attorneys

```html
<!DOCTYPE html>
<html lang="en">
<head>
<meta charset="utf-8">
<title>Bright Path Attorneys – Billboard Series</title>
<link href="https://fonts.googleapis.com/css2?family=Anton&family=Poppins:wght@400;500;600;700;800&display=swap" rel="stylesheet">
<style>
  :root {
    --page-bg: #e1e1e1;
    --board-black: #02040a;
    --board-navy: #0c1d4f;
    --streak-blue: #1f4fb8;
    --brand-green: #5ad23f;
    --text-white: #ffffff;
    --photo-navy: #1a2344;
    --photo-warm: #b48d66;
  }
  * { box-sizing: border-box; margin: 0; padding: 0; }
  html, body { width: 1200px; height: 1200px; overflow: hidden; }
  body { background: var(--page-bg); position: relative; font-family: "Poppins", sans-serif; }

  .billboard {
    position: absolute; left: 120px; width: 960px; height: 274px; overflow: hidden;
    background:
      linear-gradient(176deg, transparent 44%, rgba(31,79,184,0.45) 47%, transparent 50%),
      linear-gradient(178deg, transparent 52%, rgba(31,79,184,0.35) 54%, transparent 57%),
      radial-gradient(ellipse 60% 80% at 25% 70%, rgba(12,29,79,0.9), transparent 70%),
      linear-gradient(200deg, var(--board-navy) 0%, var(--board-black) 45%, var(--board-black) 75%, #081433 100%);
    box-shadow: 4px 6px 8px rgba(0,0,0,0.45);
  }
  .billboard--truck { top: 153px; }
  .billboard--accident { top: 463px; }
  .billboard--case { top: 773px; }

  .attorney-photo {
    position: absolute; bottom: 0; height: 260px; width: 236px;
    border-radius: 110px 110px 0 0;
    background: linear-gradient(180deg, var(--photo-warm) 0%, #8a6a4d 35%, var(--photo-navy) 62%, #10162e 100%);
  }
  .billboard--truck .attorney-photo,
  .billboard--case .attorney-photo { left: 25px; }
  .billboard--accident .attorney-photo { left: 510px; width: 200px; height: 255px; }

  .headline-poppins { position: absolute; font-weight: 800; color: var(--text-white); line-height: 1; letter-spacing: -1.5px; white-space: nowrap; }
  .subhead-poppins { position: absolute; font-weight: 700; color: var(--brand-green); line-height: 1; letter-spacing: -1px; white-space: nowrap; }
  .phone { position: absolute; font-weight: 600; letter-spacing: 3px; line-height: 1; white-space: nowrap; color: var(--text-white); }

  .brand-mark { position: absolute; display: flex; align-items: center; gap: 8px; }
  .brand-mark__square { width: 22px; height: 22px; background: var(--brand-green); }
  .brand-mark__name { font-weight: 600; font-size: 17px; color: var(--text-white); line-height: 1.05; letter-spacing: 0.5px; text-transform: uppercase; }

  /* Truck board */
  .billboard--truck .headline-poppins { left: 284px; top: 38px; font-size: 72px; }
  .billboard--truck .subhead-poppins { left: 284px; top: 110px; font-size: 48px; }
  .phone-frame { position: absolute; left: 284px; top: 186px; width: 367px; height: 52px; border: 2px solid var(--brand-green); }
  .billboard--truck .phone { left: 304px; top: 193px; font-size: 34px; }
  .billboard--truck .brand-mark { left: 682px; top: 194px; }

  /* Accident board */
  .accident-headline { position: absolute; left: 42px; top: 52px; font-family: "Anton", sans-serif; font-size: 100px; line-height: 1; color: var(--text-white); letter-spacing: 1px; }
  .billboard--accident .phone { left: 44px; top: 160px; font-size: 46px; color: var(--brand-green); }
  .billboard--accident .brand-mark { left: 736px; top: 40px; }
  .fee-rule { position: absolute; height: 2px; background: var(--brand-green); right: 0; }
  .fee-rule--top { top: 119px; left: 653px; }
  .fee-rule--bottom { top: 212px; left: 706px; }
  .fee-title { position: absolute; left: 714px; top: 125px; font-weight: 800; font-size: 60px; color: var(--text-white); line-height: 1; letter-spacing: 1px; }
  .fee-note { position: absolute; left: 714px; top: 178px; font-weight: 600; font-size: 25px; color: var(--brand-green); line-height: 1; }

  /* Case board */
  .case-line { position: absolute; left: 284px; font-family: "Anton", sans-serif; font-size: 78px; line-height: 1; letter-spacing: -0.5px; white-space: nowrap; }
  .case-line--truck { top: 38px; color: var(--text-white); }
  .case-line--case { top: 112px; color: var(--brand-green); }
  .pay-box { position: absolute; left: 680px; top: 40px; width: 227px; height: 131px; border: 2px solid var(--brand-green); }
  .pay-box__you { position: absolute; left: 18px; top: 10px; font-weight: 400; font-size: 42px; line-height: 0.95; color: var(--text-white); }
  .pay-box__amount { position: absolute; left: 128px; top: 4px; font-family: "Anton", sans-serif; font-size: 82px; line-height: 1; color: var(--brand-green); }
  .pay-box__upfront { position: absolute; left: 28px; top: 92px; font-weight: 400; font-size: 31px; letter-spacing: 3px; line-height: 1; color: var(--brand-green); }
  .billboard--case .phone { left: 284px; top: 205px; font-size: 38px; }
  .case-divider { position: absolute; left: 671px; top: 194px; width: 2px; height: 58px; background: var(--brand-green); }
  .billboard--case .brand-mark { left: 699px; top: 208px; }
</style>
</head>
<body>

<section class="billboard billboard--truck">
  <div class="attorney-photo" role="img" aria-label="Portrait of attorney Marla Benning in a navy blazer, arms crossed"></div>
  <h1 class="headline-poppins">HIT BY A TRUCK?</h1>
  <p class="subhead-poppins">NO FEE. BIG FIGHT.</p>
  <div class="phone-frame"></div>
  <p class="phone">877-GRANTLY</p>
  <div class="brand-mark"><span class="brand-mark__square"></span><span class="brand-mark__name">Bright Path<br>Attorneys</span></div>
</section>

<section class="billboard billboard--accident">
  <h1 class="accident-headline">ACCIDENT?</h1>
  <p class="phone">877-GRANTLY</p>
  <div class="attorney-photo" role="img" aria-label="Portrait of attorney Marla Benning in a navy blazer, arms crossed"></div>
  <div class="brand-mark"><span class="brand-mark__square"></span><span class="brand-mark__name">Bright Path<br>Attorneys</span></div>
  <div class="fee-rule fee-rule--top"></div>
  <p class="fee-title">NO FEE</p>
  <p class="fee-note">UNLESS WE WIN!</p>
  <div class="fee-rule fee-rule--bottom"></div>
</section>

<section class="billboard billboard--case">
  <div class="attorney-photo" role="img" aria-label="Portrait of attorney Marla Benning in a navy blazer, arms crossed"></div>
  <h1 class="case-line case-line--truck">BIG TRUCK.</h1>
  <p class="case-line case-line--case">BIG CASE.</p>
  <div class="pay-box">
    <span class="pay-box__you">YOU<br>&nbsp;PAY</span>
    <span class="pay-box__amount">$0</span>
    <span class="pay-box__upfront">UPFRONT</span>
  </div>
  <p class="phone">877-GRANTLY</p>
  <div class="case-divider"></div>
  <div class="brand-mark"><span class="brand-mark__square"></span><span class="brand-mark__name">Bright Path<br>Attorneys</span></div>
</section>

</body>
</html>
```